Design a New Business Card for Our Company

We are looking for fresh, unique, and a modern business card that reflects our roots as digital marketing agency focused on SEM.

Industry/Entity Type

Marketing

Contact Information for Business Card

looking for very unique out of the box designs. clean and modern that compliments our logo

Requirements
Must have
• colors should match our logo
• Front should have name, address, email, and phone/fax of the person, phone/fax are the same number
• back should have our url

```html
<!DOCTYPE html>
<html lang="en">
<head>
<meta charset="utf-8">
<title>Tavolen – Business Card</title>
<link rel="stylesheet" href="https://fonts.googleapis.com/css2?family=Open+Sans:wght@400;600;700&display=swap">
<style>
  :root {
    --stage: #2a2a2a;
    --brand-blue: #5f9bd3;
    --brand-blue-dark: #3d6fa8;
    --panel-grey: #b3b3b3;
    --paper: #ffffff;
    --ink-grey: #9e9e9e;
    --ink-white: #ffffff;
    --icon-blue: #4f7fb8;
  }
  * { box-sizing: border-box; margin: 0; padding: 0; }
  html, body { width: 1200px; height: 900px; overflow: hidden; }
  body {
    background: var(--stage);
    font-family: "Open Sans", Arial, sans-serif;
    position: relative;
  }
  .card {
    position: absolute;
    width: 700px;
    height: 400px;
    border-radius: 18px;
    overflow: hidden;
  }

  /* Back of card */
  .card-back {
    left: 90px;
    top: 50px;
    background: var(--brand-blue);
  }
  .card-back .brand {
    position: absolute;
    left: 0; right: 0; top: 150px;
    display: flex;
    justify-content: center;
    align-items: center;
    gap: 18px;
    color: var(--ink-white);
    font-weight: 700;
    font-size: 64px;
    letter-spacing: -1px;
    line-height: 1;
  }
  .brand-dot {
    width: 44px; height: 44px;
    border-radius: 50%;
    background: currentColor;
  }
  .card-back .web {
    position: absolute;
    left: 0; right: 0; top: 262px;
    text-align: center;
    color: var(--ink-white);
    font-size: 18px;
    letter-spacing: 4px;
  }

  /* Front of card */
  .card-front {
    left: 410px;
    top: 450px;
    background: var(--paper);
  }
  .card-front .side-panel {
    position: absolute;
    top: 0; right: 0; bottom: 0;
    width: 300px;
    background: var(--panel-grey);
  }
  .card-front .brand {
    position: absolute;
    left: 50px; top: 290px;
    display: flex;
    align-items: center;
    gap: 14px;
    color: var(--ink-grey);
    font-weight: 700;
    font-size: 48px;
    letter-spacing: -1px;
    line-height: 1;
  }
  .card-front .brand .brand-dot {
    width: 34px; height: 34px;
    background: var(--brand-blue);
  }
  .name-ribbon {
    position: absolute;
    left: 310px; top: 40px;
    width: 390px; height: 66px;
  }
  .name-band {
    position: absolute;
    left: 20px; top: 0;
    width: 370px; height: 40px;
    background: var(--brand-blue);
    color: var(--ink-white);
    font-weight: 700;
    font-size: 24px;
    text-align: right;
    padding-right: 24px;
    line-height: 40px;
  }
  .name-fold {
    position: absolute;
    left: 0; top: 0;
  }
  .person-title {
    position: absolute;
    right: 30px; top: 88px;
    color: var(--brand-blue-dark);
    font-size: 14px;
  }
  .contact {
    position: absolute;
    right: 24px; top: 190px;
    list-style: none;
    color: var(--ink-white);
    font-size: 16px;
    line-height: 24px;
  }
  .contact li {
    display: flex;
    justify-content: flex-end;
    align-items: center;
    gap: 10px;
    white-space: nowrap;
  }
  .contact .icon-slot { width: 18px; height: 18px; flex: none; }
  .contact .address-block { margin-bottom: 4px; }
</style>
</head>
<body>

<section class="card card-back" aria-label="Back of business card">
  <div class="brand"><span class="brand-dot"></span><span>tavolen</span></div>
  <p class="web">www.yourweb.com</p>
</section>

<section class="card card-front" aria-label="Front of business card">
  <div class="side-panel"></div>

  <div class="brand"><span class="brand-dot"></span><span>tavolen</span></div>

  <div class="name-ribbon">
    <svg class="name-fold" width="60" height="66" viewBox="0 0 60 66">
      <polygon points="0,0 60,0 60,40 20,40" fill="var(--brand-blue)"/>
      <polygon points="20,40 60,40 60,62" fill="var(--brand-blue-dark)"/>
    </svg>
    <div class="name-band">Your Name</div>
  </div>
  <p class="person-title">Title</p>

  <ul class="contact">
    <li>Ax-100, Road Name <span class="icon-slot"></span></li>
    <li class="address-block">Area, Country Name-10005 <span class="icon-slot"></span></li>
    <li>88-123-54321
      <svg class="icon-slot" viewBox="0 0 18 18" aria-hidden="true"><circle cx="9" cy="9" r="8" fill="none" stroke="var(--icon-blue)" stroke-width="1.5"/><path d="M6 5 Q5 9 9 12.5 Q11 13.5 12.5 12 L11 10.5 L9.8 11.2 Q7.5 9.5 7.2 7.8 L8 6.8 Z" fill="var(--icon-blue)"/></svg>
    </li>
    <li>88-123-54321
      <svg class="icon-slot" viewBox="0 0 18 18" aria-hidden="true"><rect x="4" y="2" width="10" height="6" fill="var(--icon-blue)"/><rect x="2" y="7" width="14" height="9" rx="1.5" fill="var(--icon-blue)"/><rect x="5" y="10" width="8" height="1.5" fill="#fff"/></svg>
    </li>
    <li>info@yourweb.com
      <svg class="icon-slot" viewBox="0 0 18 18" aria-hidden="true"><rect x="1.5" y="4" width="15" height="10" fill="var(--icon-blue)"/><path d="M1.5 4 L9 10 L16.5 4" fill="none" stroke="#fff" stroke-width="1.2"/></svg>
    </li>
    <li>www.yourweb.com
      <svg class="icon-slot" viewBox="0 0 18 18" aria-hidden="true"><g fill="none" stroke="var(--icon-blue)" stroke-width="1.4"><circle cx="9" cy="9" r="7.5"/><ellipse cx="9" cy="9" rx="3.5" ry="7.5"/><path d="M1.5 9 H16.5 M3 5 H15 M3 13 H15"/></g></svg>
    </li>
  </ul>
</section>

</body>
</html>
```